VELMAR WEBSITE

need to create a new website for VELMAR ltd
the company deals with all aspects of safety products & safety wear
we need a simple website to show
ideas can be taken from following website whose products we shall distribute in kenya
www.qtw.co.uk
www.brovik.eu
www.tormanhardgear.com
www.qalvenworks.co.za

we need following tabs
1) home - basic company information
2) products - broken down to following categories ie gloves, head protection, ear protection, mouth protection, foot protection
3) contacts

the company profile is a reputable company dealing with all aspects of safety, HSE (health and safety equipment), and PPE (personal protective equipment)

the website should have the brovik logo for which we are an authorized distributor.
the brovi industrial range writeup can be picked from their website

Dear Designers, i shall be able to choose a final design in 2 weeks, sorry i have not been able to finalise this due to a personal reason

Target Market(s)

the buyers are all types of industry who care for their employees safety

Industry/Entity Type

Industrial

Requirements
Must have
• clean look, fresh look, user freindly
Nice to have
• clear images, quick links etc

```html
<!DOCTYPE html>
<html lang="en">
<head>
<meta charset="utf-8">
<title>VELMAR – Specialized Protective &amp; Industrial Products</title>
<link href="https://fonts.googleapis.com/css2?family=Lato:wght@300;400;700;900&display=swap" rel="stylesheet">
<style>
:root{
  --yellow:#ffc600;
  --yellow-soft:#fff8e1;
  --ink:#333333;
  --ink-dark:#2b2b2b;
  --line:#e4e4e4;
  --card-line:#d6d6d6;
  --footer:#353535;
  --footer-line:#454545;
  --footer-text:#a9a9a9;
  --footer-head:#c9c9c9;
  --white:#ffffff;
}
*{box-sizing:border-box;margin:0;padding:0}
html,body{width:1088px;height:1200px;overflow:hidden;background:var(--white);font-family:'Lato',sans-serif;color:var(--ink)}
.page{position:relative;width:1088px;height:1200px}
.site{position:absolute;left:154px;top:0;width:781px}

.search{position:absolute;left:760px;top:1px;width:20px;height:19px;background:var(--yellow-soft);display:flex;align-items:center;justify-content:center}

.header{position:absolute;top:22px;left:0;width:781px;height:77px;background:var(--yellow)}
.brand{position:absolute;left:45px;top:0;width:152px;height:77px;background:var(--yellow-soft);display:flex;align-items:center;justify-content:center;gap:7px}
.brand-mark{width:14px;height:14px;background:var(--ink-dark)}
.brand-name{font-weight:900;font-size:22px;letter-spacing:1px;color:var(--ink-dark)}
.nav{position:absolute;right:42px;top:0;height:77px;display:flex}
.nav a{position:relative;display:block;padding:0 21px;line-height:85px;font-size:14px;font-weight:400;color:var(--ink-dark);text-decoration:none;text-transform:uppercase}
.nav a.active::before{content:"";position:absolute;left:0;right:0;top:-2px;height:4px;background:var(--ink-dark)}

.hero{position:absolute;top:99px;left:0;width:781px;height:297px;border-left:1px solid var(--line);border-right:1px solid var(--line);border-bottom:1px solid var(--line)}
.hero-tag{position:absolute;left:44px;top:27px;width:152px;height:19px;background:var(--ink-dark);border-top:2px solid var(--yellow);border-bottom:2px solid var(--yellow);color:var(--yellow);font-size:6px;font-weight:900;line-height:7px;text-align:center;padding-top:1px;letter-spacing:.3px;white-space:nowrap;overflow:hidden}
.hero-title{position:absolute;left:44px;top:96px;font-size:39px;font-weight:900;line-height:38px;color:var(--ink-dark);text-transform:uppercase}
.hero-title .accent{color:var(--yellow)}
.hero-photo{position:absolute;left:394px;top:16px;width:306px;height:281px;background:radial-gradient(ellipse at 55% 55%,#b7e24a 0%,#4a6fc4 45%,#eef0f4 75%,#ffffff 100%)}
.dots{position:absolute;right:44px;top:27px;display:flex;gap:6px}
.dots span{width:8px;height:8px;border-radius:50%;background:var(--yellow)}

.products{position:absolute;top:396px;left:0;width:781px;height:521px;border-left:1px solid var(--line);border-right:1px solid var(--line)}
.row{position:absolute;left:0;width:779px;height:260px}
.row-1{top:0;border-bottom:1px solid var(--line)}
.row-2{top:260px}
.cell{position:absolute;top:0;height:100%}
.cell+.cell{border-left:1px solid var(--line)}
.c1{left:0;width:268px}.c2{left:268px;width:246px}.c3{left:514px;width:265px}
.card{position:absolute;top:37px;width:201px;height:179px;border:1px solid var(--card-line)}
.c1 .card{left:44px}.c2 .card{left:22px}.c3 .card{left:22px}
.card-title{height:38px;margin:-1px -1px 0;background:var(--yellow);font-size:13px;font-weight:700;line-height:39px;text-align:center;text-transform:uppercase;color:var(--ink-dark)}
.card-img{position:absolute;left:50%;top:45px;transform:translateX(-50%);width:90px;height:110px;border-radius:8px}
.card-btn{position:absolute;left:60px;bottom:-11px;width:79px;height:18px;background:var(--ink);color:var(--white);font-size:10px;line-height:18px;text-align:center;text-transform:uppercase}

.img-gloves{background:linear-gradient(160deg,#f4a51c,#2b2b2b)}
.img-head{background:linear-gradient(160deg,#2c3042,#9aa3c0)}
.img-ear{background:linear-gradient(160deg,#f2cf1c,#2b2b2b)}
.img-mouth{background:linear-gradient(160deg,#6e7a84,#e8d02a)}
.img-foot{background:linear-gradient(160deg,#2a2a2a,#8c9a3a)}
.img-eye{background:linear-gradient(180deg,#ffd21a 0%,#ffd21a 25%,#dfe8ef 26%,#c7d3dc 100%)}

.footer{position:absolute;top:917px;left:0;width:781px;height:247px;background:repeating-linear-gradient(135deg,#383838 0 2px,#333333 2px 4px)}
.f-col{position:absolute;top:0;height:100%}
.f-1{left:44px;width:204px}.f-2{left:289px;width:200px}.f-3{left:537px;width:200px}
.f-head{position:absolute;top:40px;font-size:15px;font-weight:700;color:var(--footer-head);text-transform:uppercase}
.f-rule{position:absolute;left:0;width:100%;height:1px;background:var(--footer-line)}
.f-rule.r1{top:78px}.f-rule.r2{top:168px}
.f-text{position:absolute;top:92px;font-size:12px;line-height:14.5px;color:var(--footer-text);font-weight:400;white-space:nowrap}
.f-btn{position:absolute;top:190px;height:18px;padding:0 8px;background:var(--yellow);color:var(--ink-dark);font-size:10px;line-height:18px;text-transform:uppercase}
.social{position:absolute;top:107px;left:0;display:flex;gap:37px;padding-left:11px}
.social span{width:31px;height:31px;border-radius:50%;background:#262626;display:flex;align-items:center;justify-content:center}
.partners{position:absolute;top:180px;left:0;width:200px;display:flex;justify-content:space-between;align-items:center}
.partner{color:#6d6d6d;text-align:center}
.partner-name{font-size:18px;font-weight:400;line-height:18px}
.partner-sub{font-size:6px;letter-spacing:1px;text-transform:uppercase;margin-top:3px;white-space:nowrap}
.partner-own{display:flex;align-items:center;gap:4px;font-size:12px;letter-spacing:1px}
.partner-own i{width:9px;height:9px;background:#6d6d6d;display:block}

.copy-shadow{position:absolute;top:1164px;left:0;width:781px;height:36px;background:linear-gradient(180deg,#e6e6e6,#ffffff)}
.copy{position:absolute;top:1180px;left:0;width:781px;text-align:center;font-size:9px;color:#555}
</style>
</head>
<body>
<div class="page">
 <div class="site">
  <div class="search">
   <svg width="12" height="12" viewBox="0 0 12 12"><circle cx="5" cy="5" r="3.5" fill="none" stroke="#ffc600" stroke-width="2"/><line x1="7.5" y1="7.5" x2="11" y2="11" stroke="#ffc600" stroke-width="2.2"/></svg>
  </div>

  <header class="header">
   <div class="brand"><span class="brand-mark"></span><span class="brand-name">VELMAR</span></div>
   <nav class="nav">
    <a href="#">Home</a>
    <a href="#" class="active">Products</a>
    <a href="#">Contact</a>
   </nav>
  </header>

  <section class="hero">
   <div class="hero-tag">SPECIALIZED PROTECTIVE<br>&amp; INDUSTRIAL PRODUCTS</div>
   <h1 class="hero-title">Good<br>Products<br><span class="accent">Great Prices</span></h1>
   <div class="hero-photo" role="img" aria-label="Worker in hard hat, safety goggles, ear muffs, gloves and hi-vis vest giving thumbs up"></div>
   <div class="dots"><span></span><span></span><span></span></div>
  </section>

  <section class="products">
   <div class="row row-1">
    <div class="cell c1"><div class="card"><div class="card-title">Gloves</div><div class="card-img img-gloves" role="img" aria-label="Orange and black work glove"></div><div class="card-btn">View</div></div></div>
    <div class="cell c2"><div class="card"><div class="card-title">Head Protection</div><div class="card-img img-head" role="img" aria-label="Welding helmet"></div><div class="card-btn">View</div></div></div>
    <div class="cell c3"><div class="card"><div class="card-title">Ear Protection</div><div class="card-img img-ear" role="img" aria-label="Yellow helmet-mounted ear muffs"></div><div class="card-btn">View</div></div></div>
   </div>
   <div class="row row-2">
    <div class="cell c1"><div class="card"><div class="card-title">Mouth Protection</div><div class="card-img img-mouth" role="img" aria-label="Respirator mask with goggles"></div><div class="card-btn">View</div></div></div>
    <div class="cell c2"><div class="card"><div class="card-title">Foot Protection</div><div class="card-img img-foot" role="img" aria-label="Black safety boot"></div><div class="card-btn">View</div></div></div>
    <div class="cell c3"><div class="card"><div class="card-title">Eye Protection</div><div class="card-img img-eye" role="img" aria-label="Yellow visor with clear face shield"></div><div class="card-btn">View</div></div></div>
   </div>
  </section>

  <footer class="footer">
   <div class="f-col f-1">
    <div class="f-head">Customer Services</div>
    <div class="f-rule r1"></div>
    <div class="f-text">Our Distribution<br>Useful Links<br>Advanced Search<br>Knowledge Base</div>
    <div class="f-rule r2"></div>
    <div class="f-btn">Read More</div>
   </div>
   <div class="f-col f-2">
    <div class="f-head">Contact</div>
    <div class="f-rule r1"></div>
    <div class="f-text">48 Kiln Road<br>Tarvel, KD 410385<br>E-mail: info@velmar.com<br>Telephone: +1 800 555 0142</div>
    <div class="f-rule r2"></div>
    <div class="f-btn">Contact Us</div>
   </div>
   <div class="f-col f-3">
    <div class="f-head">Share</div>
    <div class="f-rule r1"></div>
    <div class="social">
     <span aria-label="Share on social network"></span>
     <span aria-label="Share on social network"></span>
     <span aria-label="Share by email"><svg width="15" height="11" viewBox="0 0 15 11"><rect x="0.5" y="0.5" width="14" height="10" rx="1" fill="#a9a9a9"/><polyline points="1,1.5 7.5,6.5 14,1.5" fill="none" stroke="#262626" stroke-width="1.4"/></svg></span>
    </div>
    <div class="f-rule r2"></div>
    <div class="partners">
     <div class="partner"><div class="partner-name">Brovik</div><div class="partner-sub">Authorized Distributor</div></div>
     <div class="partner partner-own"><i></i>VELMAR</div>
    </div>
   </div>
  </footer>

  <div class="copy-shadow"></div>
  <div class="copy">© 2013 - Velmar</div>
 </div>
</div>
</body>
</html>
```